Accountability Project Graphics

I want to create 10 social media graphics (new Instagram size 4:5 (1080 x 1350 pixels) focusing on our Kelmora Accountability App, using any of the 3 pictures attached. Use the attached pics only, NO RANDOM STOCK PHOTOGRAPHY. For the color scheme, use the landing page colors/fonts (attached).
You can add any of the 3 photos attached but I mainly need BOLD text that includes these headlines and sub-headlines on them.
Please NOTE for all the headlines below, also add this sub-headline on each graphic:
Stay Consistent with MB in Your Pocket!
Here are the headlines:
• Stop Starting Over Every Monday
• You don't need more willpower. You need more support
• Built for women who are tired of doing this alone
• When Motivation Fades, MB Checks In
• The Support System You've Been Missing
• Support When Motivation Disappears
• What if MB Checked in Every Day?
• The Missing Piece Isn't Another Diet
• Eat the food you love. Stay accountable every day.
• One Bad Meal Doesn't Mean You Failed
women over 40 trying to lose weight

```html
<!DOCTYPE html>
<html lang="en">
<head>
<meta charset="utf-8">
<title>Kelmora Accountability App – Social Graphics</title>
<link rel="stylesheet" href="https://fonts.googleapis.com/css2?family=Gelasio:wght@600;700&family=Inter:wght@600&display=swap">
<style>
  :root {
    --canvas: #f5f5f5;
    --card-top: #fbe6ea;
    --card-bottom: #f8dde3;
    --box: #fdf6f7;
    --plum: #2b1a3b;
    --rose: #c5557f;
    --ink: #111111;
    --photo-pink: #e89bb8;
    --photo-denim: #5b6f94;
    --photo-dark: #2c2f3d;
  }
  * { margin: 0; padding: 0; box-sizing: border-box; }
  html, body { width: 1200px; height: 1103px; overflow: hidden; }
  body { background: var(--canvas); position: relative; font-family: "Gelasio", Georgia, serif; }

  .post {
    position: absolute;
    width: 222px;
    height: 278px;
    background: linear-gradient(180deg, var(--card-top), var(--card-bottom));
    overflow: hidden;
  }
  .headline-box {
    position: absolute;
    left: 11px; right: 11px; top: 12px;
    min-height: 75px;
    background: var(--box);
    border-radius: 8px;
    padding: 7px 7px 8px;
    z-index: 2;
  }
  .headline {
    font-weight: 700;
    font-size: 17.5px;
    line-height: 1.08;
    color: var(--plum);
    letter-spacing: 0.1px;
  }
  .headline.compact { font-size: 16px; line-height: 1.1; }
  .headline .accent { color: var(--rose); }
  .subline {
    font-family: "Inter", Arial, sans-serif;
    font-weight: 600;
    font-size: 7.2px;
    color: var(--ink);
    margin-top: 6px;
  }
  .photo {
    position: absolute;
    bottom: 0;
    z-index: 1;
    border-radius: 40% 40% 0 0;
  }
  .photo.hug {
    left: 32px; width: 150px; top: 104px;
    background: linear-gradient(90deg, #f3f1e8 0%, #2e2740 35%, var(--photo-pink) 70%, #e46fa0 100%);
    opacity: 0.75;
  }
  .photo.duo {
    left: 22px; width: 180px; top: 92px;
    background: linear-gradient(90deg, var(--photo-dark) 0%, #f2efee 30%, var(--photo-denim) 60%, #3f5178 100%);
    opacity: 0.7;
  }
  .photo.solo {
    left: 66px; width: 96px; top: 90px;
    background: linear-gradient(180deg, #3a2a2a 0%, var(--photo-dark) 35%, #1e2130 100%);
    opacity: 0.8;
  }

  .r1 { top: 67px; }
  .r2 { top: 411px; }
  .r3 { top: 753px; }
</style>
</head>
<body>

  <!-- Row 1 -->
  <section class="post r1" style="left:75px">
    <div class="headline-box">
      <h2 class="headline">Stop Starting Over <span class="accent">Every Monday</span></h2>
      <p class="subline">Stay Consistent with MB in Your Pocket!</p>
    </div>
    <div class="photo hug" role="img" aria-label="Photo of two women sharing a joyful hug"></div>
  </section>

  <section class="post r1" style="left:328px">
    <div class="headline-box">
      <h2 class="headline compact">You don't need more willpower. <span class="accent">You need more support</span></h2>
      <p class="subline">Stay Consistent with MB in Your Pocket!</p>
    </div>
    <div class="photo hug" role="img" aria-label="Photo of two women sharing a joyful hug"></div>
  </section>

  <section class="post r1" style="left:593px">
    <div class="headline-box">
      <h2 class="headline compact">Built for women who are tired of <span class="accent">doing this alone</span></h2>
      <p class="subline">Stay Consistent with MB in Your Pocket!</p>
    </div>
    <div class="photo hug" role="img" aria-label="Photo of two women sharing a joyful hug"></div>
  </section>

  <!-- Row 2 -->
  <section class="post r2" style="left:75px">
    <div class="headline-box">
      <h2 class="headline">When Motivation Fades, <span class="accent">MB Checks In</span></h2>
      <p class="subline">Stay Consistent with MB in Your Pocket!</p>
    </div>
    <div class="photo duo" role="img" aria-label="Photo of two smiling women in denim standing side by side"></div>
  </section>

  <section class="post r2" style="left:328px">
    <div class="headline-box">
      <h2 class="headline">The Support System <span class="accent">You've Been Missing</span></h2>
      <p class="subline">Stay Consistent with MB in Your Pocket!</p>
    </div>
    <div class="photo duo" role="img" aria-label="Photo of two smiling women in denim standing side by side"></div>
  </section>

  <section class="post r2" style="left:594px">
    <div class="headline-box">
      <h2 class="headline compact">Support When <span class="accent">Motivation Disappears</span></h2>
      <p class="subline">Stay Consistent with MB in Your Pocket!</p>
    </div>
    <div class="photo duo" role="img" aria-label="Photo of two smiling women in denim standing side by side"></div>
  </section>

  <section class="post r2" style="left:866px">
    <div class="headline-box">
      <h2 class="headline compact">What if MB Checked in <span class="accent">Every Day?</span></h2>
      <p class="subline">Stay Consistent with MB in Your Pocket!</p>
    </div>
    <div class="photo duo" role="img" aria-label="Photo of two smiling women in denim standing side by side"></div>
  </section>

  <!-- Row 3 -->
  <section class="post r3" style="left:73px">
    <div class="headline-box">
      <h2 class="headline compact">The Missing Piece <span class="accent">Isn't Another Diet</span></h2>
      <p class="subline">Stay Consistent with MB in Your Pocket!</p>
    </div>
    <div class="photo solo" role="img" aria-label="Photo of a smiling woman in a black outfit, hand on hip"></div>
  </section>

  <section class="post r3" style="left:328px">
    <div class="headline-box">
      <h2 class="headline compact">Eat the food you love. <span class="accent">Stay accountable every day.</span></h2>
      <p class="subline">Stay Consistent with MB in Your Pocket!</p>
    </div>
    <div class="photo solo" role="img" aria-label="Photo of a smiling woman in a black outfit, hand on hip"></div>
  </section>

  <section class="post r3" style="left:596px">
    <div class="headline-box">
      <h2 class="headline compact">One Bad Meal <span class="accent">Doesn't Mean You Failed</span></h2>
      <p class="subline">Stay Consistent with MB in Your Pocket!</p>
    </div>
    <div class="photo solo" role="img" aria-label="Photo of a smiling woman in a black outfit, hand on hip"></div>
  </section>

</body>
</html>
```